Gestalten Sie ein tolles Selbstliebe-Buchcover
Design kam bei der Zielgruppe sehr gut an und war professionell umgesetzt. Die Kommunikation läuft zielgerichtet und nett und ich habe schnell alle Dateien bekommen, die ich brauche. Vielen Dank!
Hallo,
schön, dass Sie sich für diese Ausschreibung interessieren. Wir suchen ein Cover für unser Buch, das wir im Selbstverlag veröffentlichen werden.
Titel: Mondgarten am Nordufer
Untertitel 1: Wie du dich von negativen Gedanken befreist und eine liebevolle Beziehung zu dir selbst aufbaust
Untertitel Teil 2: 12 lebensverändernde Monate voller positiver Impulse und Liebe für dich
Das Buch soll (mehrheitlich) Frauen unterstützen, eine liebevolle Beziehung zu sich selbst aufzubauen, negative Gedanken loszulassen und innere Ruhe zu finden.
Aufgabenstellung
Wir sind für jegliche Vorschläge im Rahmen des Themas, der Samples und der Schieberegler offen.
Wichtig ist allerdings
- dass das Design selbst in der kleinen Ansicht (Suchergebnisse) auf Vendora klar hervorsticht, das heißt dort klar erkennbar und die Schrift sofort lesbar ist. Es muss in klein „wirken“, weil viele mit dem Handy auf Vendora shoppen und die Ansicht in den Suchergebnissen dort noch kleiner ist.
- dass das Design die gezielt Emotionen vermittelt
Optimal wäre es, wenn Ihr keine Mockups hochladet. Das macht es viel schwieriger, die Designs einzuschätzen und miteinander zu vergleichen.

```html
<!DOCTYPE html>
<html lang="de">
<head>
<meta charset="utf-8">
<title>Mondgarten am Nordufer – Buchcover</title>
<link rel="stylesheet" href="https://fonts.googleapis.com/css2?family=Fraunces:opsz,wght@9..144,800;9..144,900&family=Comfortaa:wght@600;700&display=swap">
<style>
  :root {
    --stage: #d8d9db;
    --paper: #e5e4e7;
    --navy: #2a3384;
    --lavender: #a7a8dc;
    --sky: #2068a6;
    --coral: #ea6a58;
    --white: #ffffff;
  }
  * { box-sizing: border-box; margin: 0; padding: 0; }
  html, body {
    width: 1200px;
    height: 960px;
    overflow: hidden;
    background: var(--stage);
  }
  .cover {
    position: absolute;
    left: 290px;
    top: 30px;
    width: 620px;
    height: 900px;
    background: var(--paper);
    overflow: hidden;
    box-shadow: 0 10px 30px rgba(0,0,0,0.12);
  }
  .cover__band {
    position: absolute;
    inset: 0;
    width: 620px;
    height: 900px;
  }
  .cover__author {
    position: absolute;
    top: 64px;
    width: 100%;
    text-align: center;
    font-family: "Comfortaa", sans-serif;
    font-weight: 700;
    font-size: 17px;
    letter-spacing: 0.18em;
    color: var(--white);
  }
  .cover__title {
    position: absolute;
    top: 100px;
    width: 100%;
    text-align: center;
    font-family: "Fraunces", serif;
    font-weight: 900;
    color: var(--lavender);
    line-height: 0.95;
  }
  .cover__title-main { display: block; font-size: 84px; }
  .cover__title-sub { display: block; font-size: 66px; }
  .cover__subtitle {
    position: absolute;
    top: 292px;
    left: 90px;
    width: 440px;
    text-align: center;
    font-family: "Comfortaa", sans-serif;
    font-weight: 700;
    font-size: 18px;
    line-height: 1.35;
    color: var(--white);
  }
  .cover__figure {
    position: absolute;
    left: 160px;
    top: 430px;
    width: 330px;
    height: 360px;
  }
  .cover__tagline {
    position: absolute;
    bottom: 40px;
    width: 100%;
    text-align: center;
    font-family: "Comfortaa", sans-serif;
    font-weight: 700;
    font-size: 19px;
    line-height: 1.4;
    color: var(--navy);
  }
</style>
</head>
<body>
  <main class="cover">
    <svg class="cover__band" viewBox="0 0 620 900" aria-hidden="true">
      <path fill="var(--navy)" d="M0,0 H620 V110 C585,150 600,220 575,290 C555,350 530,400 490,440 C455,475 430,500 380,520 L250,520 C200,545 150,480 95,440 C55,410 25,395 0,390 Z"/>
    </svg>

    <p class="cover__author">NAME AUTOR*IN</p>

    <h1 class="cover__title">
      <span class="cover__title-main">Mondgarten</span>
      <span class="cover__title-sub">am Nordufer</span>
    </h1>

    <p class="cover__subtitle">Wie du dich von negativen Gedanken befreist und eine liebevolle Beziehung zu dir selbst aufbaust</p>

    <svg class="cover__figure" viewBox="0 0 330 360" role="img" aria-label="Illustration: sitzende Frau mit langem blauem Haar, die ein großes rotes Herz umarmt">
      <defs>
        <linearGradient id="figureTone" x1="0" y1="0" x2="0" y2="1">
          <stop offset="0" stop-color="var(--navy)"/>
          <stop offset="0.45" stop-color="var(--sky)"/>
          <stop offset="0.75" stop-color="var(--coral)"/>
          <stop offset="1" stop-color="var(--navy)"/>
        </linearGradient>
      </defs>
      <rect x="0" y="0" width="330" height="360" rx="160" fill="url(#figureTone)"/>
    </svg>

    <p class="cover__tagline">12 lebensverändernde Monate voller<br>positiver Impulse und Liebe für dich</p>
  </main>
</body>
</html>
```